Indian Takeaway Menu -

I would like to have double parallel fold A4 sheet menu.
A4 sheet cut in half and attached to the other half to make the sheet 4 small pages long.

Colors
abd036
ffffff

Requirements
Must have
• Please check new attachments - menu size and layout is not correct.
• I would like to add Dark brown colour. A4 sheet folded 4x Menu layout pocket size.
Nice to have
• Dark Brown - Parrot Green and very light Brown

```html
<!DOCTYPE html>
<html lang="en">
<head>
<meta charset="utf-8">
<title>Saffron Hearth – Takeaway Menu</title>
<link rel="stylesheet" href="https://fonts.googleapis.com/css2?family=Crimson+Text:wght@400;600;700&family=Kaushan+Script&family=Patrick+Hand&family=Oswald:wght@500&display=swap">
<style>
:root{
  --brown:#4a2817;
  --brown-deep:#3a1f12;
  --parrot:#abd036;
  --olive:#6f8f34;
  --olive-dark:#5d7a2b;
  --cream:#f4efe6;
  --paper:#ffffff;
  --ink:#2d2a26;
  --muted:#5e5850;
  --red:#d8321f;
  --amber:#f4b81c;
  --stage:#fbfbfb;
}
*{box-sizing:border-box;margin:0;padding:0}
html,body{width:800px;height:1200px;overflow:hidden;background:var(--stage)}
body{font-family:"Crimson Text",Georgia,serif;color:var(--ink);position:relative}

.side-label{position:absolute;left:0;width:800px;text-align:center;font-family:"Crimson Text",Georgia,serif;font-size:22px;letter-spacing:1px;color:#222}
.side-label.front{top:222px}
.side-label.back{top:590px}

.sheet{position:absolute;left:10px;width:780px;height:280px;display:grid;grid-template-columns:repeat(4,1fr);background:var(--paper);box-shadow:0 10px 8px -4px rgba(0,0,0,.28)}
.sheet.front{top:262px}
.sheet.back{top:630px;background:linear-gradient(180deg,#f7f5f2,#eceae6)}
.panel{position:relative;padding:6px 7px;overflow:hidden}

.section-tag{display:inline-block;background:var(--brown);color:#fff;font-family:"Kaushan Script",cursive;font-size:7.5px;padding:1px 6px;margin:3px 0 3px;border-bottom:1px solid var(--brown-deep)}
.section-tag.wide{display:block;font-size:7px;padding:3px 6px;line-height:1.3}

.item{margin-bottom:3px}
.item .row{display:grid;grid-template-columns:1fr 34px 22px;font-size:6px;line-height:7px;color:var(--ink)}
.item .code{text-align:center}
.item .price{text-align:right}
.item .desc{font-size:4.3px;line-height:5px;color:var(--muted);padding-left:6px}

.photo{border-radius:1px}
.photo.curry{height:62px;margin-top:4px;background:linear-gradient(90deg,#e9d6b2 0%,#d8b07a 35%,#a43a1c 55%,#c9541f 80%,#6c2b14 100%)}
.photo.naan{height:70px;margin:4px 0;background:radial-gradient(ellipse at 50% 55%,#f1d476 0%,#e2b44c 45%,#a77631 80%,#3b2c22 100%)}
.photo.spread{position:absolute;left:7px;right:7px;bottom:6px;height:46px;background:linear-gradient(90deg,#e2c488,#c7853a 40%,#8f4a22 70%,#d8b778)}

.bread-list .row{grid-template-columns:1fr 30px 22px;font-size:5.6px;line-height:7px}

/* cover */
.cover{padding:0;display:flex;flex-direction:column;background:#fff}
.brand{text-align:center;padding-top:22px}
.brand-name{font-family:"Crimson Text",Georgia,serif;font-weight:700;font-size:22px;color:var(--brown);line-height:1}
.brand-tag{font-size:5px;letter-spacing:1px;color:var(--brown);margin-top:2px}
.cooked-band{margin:8px 6px 0;background:var(--brown);color:#fff;font-family:"Patrick Hand",cursive;font-size:7.5px;text-align:center;padding:2px 0}
.cover-photo{margin:0 6px;height:90px;background:linear-gradient(90deg,#6b4a2e,#b98447 20%,#7c5436 38%,#c2924f 55%,#8a5a30 72%,#d09a4c 88%,#5b3a22)}
.cover-info{position:relative;height:52px;margin:0 6px}
.hours{position:absolute;left:2px;top:8px;width:128px;height:36px;border:1px solid #999;border-radius:14px;padding:3px 8px;font-family:"Patrick Hand",cursive}
.hours h3{font-weight:400;color:var(--red);font-size:8.5px;line-height:9px}
.hours p{font-size:6px;line-height:7px;color:#222}
.ribbon{position:absolute;right:2px;top:0;width:36px;height:44px;background:var(--amber);clip-path:polygon(0 0,100% 0,100% 100%,50% 84%,0 100%);text-align:center;font-family:"Patrick Hand",cursive;font-size:5.2px;line-height:6px;padding-top:6px;color:#3a2514}
.cover-foot{margin:auto 6px 6px;height:22px;background:var(--brown);display:flex;align-items:center;justify-content:space-around;color:#fff;font-size:4.5px;position:relative}
.foot-item{display:flex;flex-direction:column;align-items:center;gap:1px}
.foot-item svg{width:8px;height:8px}

/* back panels */
.green-panel{background:var(--olive);color:#fff;margin:4px;padding:4px 5px}
.allergens{font-size:4.6px;line-height:6px;border-bottom:1px solid rgba(255,255,255,.4);padding-bottom:3px}
.deal-tag{display:inline-block;background:#f2ecd8;color:var(--brown);font-family:"Kaushan Script",cursive;font-size:6px;padding:1px 6px;margin:4px 0 2px}
.deal-sub{color:#f6d8cf;font-size:4.6px}
.deal-item .row{font-size:5px;line-height:6px;display:grid;grid-template-columns:1fr 18px;color:#fff}
.deal-item .row .price{text-align:right;color:#f3c1b5}
.deal-item .desc{font-size:3.8px;line-height:4.6px;color:#e3ecd1;margin-bottom:2px}
.set-meals{display:grid;grid-template-columns:repeat(3,1fr);gap:3px;margin-top:5px}
.set-meal{border:1px solid rgba(255,255,255,.6);padding:3px;font-size:4.6px;line-height:5.8px;text-align:left}
.set-meal h4{font-weight:400;text-align:center;font-size:5px;line-height:5.6px;margin-bottom:3px}

.legend{background:var(--parrot);color:#3a4a10;font-size:4.8px;line-height:6px;padding:2px 5px;margin:3px 0}
.back .item .row{font-size:5.2px;line-height:6px}
.back .item .desc{font-size:3.8px;line-height:4.5px}
.back .item{margin-bottom:2px}
</style>
</head>
<body>

<div class="side-label front">FRONT</div>

<section class="sheet front" aria-label="Menu outer side">
  <!-- Lamb & prawn -->
  <div class="panel">
    <div class="section-tag">Lamb Dishes</div>
    <div class="item"><div class="row"><span>Lamb Madras</span><span class="code"></span><span class="price">€10.95</span></div><div class="desc">The popular dish of madras cooked with plum tomato, degi chilli, coconut and finished with hint of lemon juice</div></div>
    <div class="item"><div class="row"><span>Palak Gosht</span><span class="code">3,y</span><span class="price">€10.95</span></div><div class="desc">Pan fried lamb pieces cooked with spinach, fresh herbs, ginger and touch of cream</div></div>
    <div class="item"><div class="row"><span>Lamb Roganjosh</span><span class="code"></span><span class="price">€10.95</span></div><div class="desc">Slow cooked tender lamb in kashmiri style with fresh herbs and Himalayan spices</div></div>
    <div class="item"><div class="row"><span>Lamb Kohlapuri</span><span class="code">3,4,5</span><span class="price">€10.95</span></div><div class="desc">Lamb dish from South Coast of India flavoured with yoghurt, nuts and coconut</div></div>
    <div class="item"><div class="row"><span>Lamb Jalferzi</span><span class="code">3,5</span><span class="price">€10.95</span></div><div class="desc">Lamb, tossed with cubes of onions, peppers flavored with crushed coriander seeds and dry fenugreek with hint of cream</div></div>
    <div class="item"><div class="row"><span>Gosht Biryani</span><span class="code">3,5,y</span><span class="price">€11.00</span></div><div class="desc">Aged rice cooked with tender lamb brown onions, house made masala and accompanied with curry sauce.</div></div>
    <div class="section-tag">Prawn Dishes</div>
    <div class="item"><div class="row"><span>Prawn Masala</span><span class="code">3</span><span class="price">€11.95</span></div><div class="desc">Prawns in a smooth creamy sauce flavoured with kasoori methi &amp; tandoori spices</div></div>
    <div class="photo curry" role="img" aria-label="Photo of naan bread beside a bowl of red curry"></div>
  </div>

  <!-- Prawn & vegetarian -->
  <div class="panel">
    <div class="item"><div class="row"><span>Prawn Karahi</span><span class="code"></span><span class="price">€11.95</span></div><div class="desc">Prawns cooked with peppers, spring onion, caramelised onion, tomatoes &amp; whole spices</div></div>
    <div class="item"><div class="row"><span>Goan Prawn Curry</span><span class="code">3,4,5</span><span class="price">€11.95</span></div><div class="desc">Fisherman's favourite prawn curry aromatic with coconut, mustard, nuts, curry leaves and spices from goa's costal area</div></div>
    <div class="item"><div class="row"><span>Prawn Bhuna</span><span class="code">LF</span><span class="price">€11.95</span></div><div class="desc">Prawns cooked in onions &amp; tomato with black pepper to bought together the kick of spices</div></div>
    <div class="item"><div class="row"><span>Prawn Biryani</span><span class="code">3,6,y</span><span class="price">€11.95</span></div><div class="desc">Pan fried prawn cooked with egg, green peas &amp; onion served with curry sauce</div></div>
    <div class="photo naan" role="img" aria-label="Photo of golden garlic naan topped with herbs"></div>
    <div class="section-tag">Vegetarian Dishes</div>
    <div class="item"><div class="row"><span>Shahi Paneer</span><span class="code">3,5</span><span class="price">€8.95</span></div><div class="desc">Indian cheese in semi-dry sauce</div></div>
    <div class="item"><div class="row"><span>Subz Maloni Mild</span><span class="code"></span><span class="price">€8.95</span></div><div class="desc">Stir fried vegetables with ground spices</div></div>
  </div>

  <!-- Veg & bread -->
  <div class="panel">
    <div class="item"><div class="row"><span>Saag Paneer</span><span class="code">3,y</span><span class="price">€8.95</span></div><div class="desc">Pan fried cottage cheese &amp; spinach with kasoori methi &amp; fresh coriander</div></div>
    <div class="item"><div class="row"><span>Sambhar Vegetable Curry</span><span class="code">4,y v</span><span class="price">€8.95</span></div><div class="desc">Vegetable curry cooked with lentil, curry leaves, and mustard seeds</div></div>
    <div class="item"><div class="row"><span>Vegetable Biryani</span><span class="code">3,5,y v</span><span class="price">€8.95</span></div><div class="desc">Basmati Rice cooked with vegetables, fresh herbs, spices &amp; fried golden onion. Comes with curry sauce</div></div>
    <div class="item"><div class="row"><span>Dum Wale Aloo</span><span class="code">3</span><span class="price">€8.95</span></div><div class="desc">Potatoes cooked with ginger, garlic, onions, yoghurt &amp; curry leave with cumin flavored.</div></div>
    <div class="item"><div class="row"><span>Karahi Paneer</span><span class="code">3</span><span class="price">€8.95</span></div><div class="desc">Colorful curry is prepared using homemade Indian cheese (paneer)</div></div>
    <div class="section-tag wide">Nan Bread &amp; Side Orders All naan bread contains 2,3,6</div>
    <div class="bread-list">
      <div class="item"><div class="row"><span>Naan</span><span class="code"></span><span class="price">€2.20</span></div></div>
      <div class="item"><div class="row"><span>Garlic Naan</span><span class="code"></span><span class="price">€2.50</span></div></div>
      <div class="item"><div class="row"><span>Garlic Chilli Naan</span><span class="code"></span><span class="price">€3.00</span></div></div>
      <div class="item"><div class="row"><span>Peshwari Naan</span><span class="code">5</span><span class="price">€3.00</span></div></div>
      <div class="item"><div class="row"><span>Keema Naan</span><span class="code"></span><span class="price">€3.00</span></div></div>
      <div class="item"><div class="row"><span>Coriander Naan</span><span class="code"></span><span class="price">€2.50</span></div></div>
      <div class="item"><div class="row"><span>Chilli Cheese Naan</span><span class="code">3</span><span class="price">€3.00</span></div></div>
      <div class="item"><div class="row"><span>G.O.C</span><span class="code"></span><span class="price">€3.00</span></div></div>
      <div class="item"><div class="row"><span>Boiled Basmati</span><span class="code"></span><span class="price">€2.00</span></div></div>
      <div class="item"><div class="row"><span>Pilau Rice</span><span class="code"></span><span class="price">€2.00</span></div></div>
      <div class="item"><div class="row"><span>Lemon Rice</span><span class="code">4</span><span class="price">€3.00</span></div></div>
      <div class="item"><div class="row"><span>Poppodum(2)</span><span class="code"></span><span class="price">€2.50</span></div></div>
      <div class="item"><div class="row"><span>Riata</span><span class="code">3</span><span class="price">€2.50</span></div></div>
    </div>
  </div>

  <!-- Cover -->
  <div class="panel cover">
    <div class="brand">
      <div class="brand-name">Saffron Hearth</div>
      <div class="brand-tag">AUTHENTIC INDIAN FOOD AT HOME</div>
    </div>
    <div class="cooked-band">ALL OUR MEALS ARE COOKED TO ORDER</div>
    <div class="cover-photo" role="img" aria-label="Photo strip of whole spices and ground spices in bowls"></div>
    <div class="cover-info">
      <div class="hours">
        <h3>OPENING HOURS:</h3>
        <p>SUN - THURS 5PM TO 10:00PM</p>
        <p>FRI - SAT 5:00PM-10:30PM</p>
      </div>
      <div class="ribbon">DELIVERIES<br>FROM<br>5:30PM</div>
    </div>
    <div class="cover-foot">
      <div class="foot-item">
        <svg viewBox="0 0 10 10" aria-hidden="true"><circle cx="5" cy="5" r="5" fill="#f0a020"/><path d="M3.3 2.6l1 1-.5.7c.4.8.9 1.3 1.7 1.7l.7-.5 1 1-.6.9c-1.9-.3-3.5-1.9-3.8-3.8z" fill="#fff"/></svg>
        <span>016 480 2271</span>
      </div>
      <div class="foot-item">
        <svg viewBox="0 0 10 10" aria-hidden="true"><circle cx="5" cy="5" r="5" fill="#f0a020"/><path d="M3.3 2.6l1 1-.5.7c.4.8.9 1.3 1.7 1.7l.7-.5 1 1-.6.9c-1.9-.3-3.5-1.9-3.8-3.8z" fill="#fff"/></svg>
        <span>016 480 2273</span>
      </div>
      <div class="foot-item">
        <svg viewBox="0 0 10 10" aria-hidden="true"><circle cx="5" cy="5" r="5" fill="#f0a020"/><circle cx="5" cy="5" r="2.6" fill="none" stroke="#fff" stroke-width=".8"/><path d="M2.4 5h5.2M5 2.4v5.2" stroke="#fff" stroke-width=".6"/></svg>
        <span>www.saffronhearth.ie</span>
      </div>
    </div>
  </div>
</section>

<div class="side-label back">BACK</div>

<section class="sheet back" aria-label="Menu inner side">
  <!-- Allergens, deals, set meals -->
  <div class="panel" style="padding:0">
    <div class="green-panel" style="height:272px">
      <div class="allergens">1 Celery &nbsp;2 Gluten &nbsp;3 Dairy &nbsp;4 Mustard &nbsp;5 Nuts &nbsp;6 Egg &nbsp;7 fish<br>8 Soya &nbsp;9 Peanuts &nbsp;10 Lupin &nbsp;11 Sulpher Dioxide &nbsp;12 Mollusc<br>13 Sesame Seeds &nbsp;14 Crustaceans</div>
      <div class="deal-tag">Meal Deals only €8.50</div>
      <div class="deal-sub">Chose Fav Dishes</div>
      <div class="deal-item"><div class="row"><span>Choose with Rice or Plain Naan Chicken Dopiaza</span><span class="price"></span></div><div class="desc">Chicken cooked with ginger and chunks of onions and finished with cumin seeds</div></div>
      <div class="deal-item"><div class="row"><span>Chicken Rogan josh</span><span class="price">€8.50</span></div><div class="desc">A red chicken curry prepared with fresh herbs &amp; spices, a delicacy from Kashmir</div></div>
      <div class="deal-item"><div class="row"><span>Chicken Bhuna</span><span class="price">€8.50</span></div><div class="desc">Tomatoes and onion sauce cooked with black peppers &amp; spring onions</div></div>
      <div class="deal-item"><div class="row"><span>Tarkari Makhani</span><span class="price">€8.50</span></div><div class="desc">Mixed seasonal vegetables in a smooth tikka masala sauce</div></div>
      <div class="set-meals">
        <div class="set-meal"><h4>SET MEAL 1<br>€16.00</h4>Onion bhajia<br>Chicken Tikka Masala<br>Pilau rice<br>Naan<br>Poppadoms</div>
        <div class="set-meal"><h4>SET MEAL 2<br>€27.00</h4>Onion bhajia<br>Chicken tikka<br>Chicken Tikka Masala<br>Lamb Roganjosh<br>2xPilau rice<br>1xNaan<br>Poppadom</div>
        <div class="set-meal"><h4>SET MEAL 3/4<br>€43.00</h4>Onion bhajia<br>Vegetable samosa<br>Chicken tikka<br>Chicken Tikka Masala<br>Sambhar Veg Curry<br>2 x Pilau Rice<br>2 x Naan</div>
      </div>
    </div>
  </div>

  <!-- Sides & starters -->
  <div class="panel">
    <div class="section-tag">Healthy Side orders</div>
    <div class="item"><div class="row"><span>Sautéed Broccoli</span><span class="code">v</span><span class="price">€5.00</span></div><div class="desc">Broccoli, green beans and spinach leaves sautéed with roasted cumin and fresh garlic.</div></div>
    <div class="item"><div class="row"><span>Chana Saag</span><span class="code">3 y v</span><span class="price">€5.00</span></div><div class="desc">Chickpeas cooked with chopped spinach, onion and cumin and finished with cream.</div></div>
    <div class="item"><div class="row"><span>Chana Masala</span><span class="code">v</span><span class="price">€5.00</span></div><div class="desc">Chickpeas simmered with tomato, caramelised onion, black pepper and fresh coriander</div></div>
    <div class="item"><div class="row"><span>Aloo Saag</span><span class="code">3 y v</span><span class="price">€5.00</span></div><div class="desc">Crispy Potato with spinach, coriander, garam masala and a dash of cream</div></div>
    <div class="item"><div class="row"><span>Aloo Ghobi</span><span class="code">v</span><span class="price">€5.00</span></div><div class="desc">Crispy Potatoes cubes &amp; Cauliflower cooked with roasted cumin and onion gravy.</div></div>
    <div class="item"><div class="row"><span>Tarka Daal</span><span class="code">4 y v</span><span class="price">€5.00</span></div><div class="desc">Home style cooked yellow chana cooked with cumin &amp; garam masala</div></div>
    <div class="item"><div class="row"><span>Tangy Aloo</span><span class="code">v</span><span class="price">€5.00</span></div><div class="desc">Crispy Potatoes cubes cooked with roasted cumin and touch of tangy sauce</div></div>
    <div class="legend">V: Can be cooked without allergen &nbsp;H: Healthy Option<br>V: Suitable for Vegans</div>
    <div class="section-tag">Starters</div>
    <div class="item"><div class="row"><span>Onion Bhajia</span><span class="code">6</span><span class="price">€4.50</span></div><div class="desc">Spinach &amp; onions fritters flavoured with mild spices</div></div>
    <div class="item"><div class="row"><span>Vegetable Samosa</span><span class="code">2</span><span class="price">€4.50</span></div><div class="desc">Crispy Pastry stuffed with potatoes, chick peas, green peas mixed with ideal spices</div></div>
    <div class="item"><div class="row"><span>Palak Tikki</span><span class="code">v</span><span class="price">€4.50</span></div><div class="desc">Cakes of fresh spinach and chana dal</div></div>
    <div class="item"><div class="row"><span>Veg Pakora</span><span class="code">v</span><span class="price">€5.00</span></div><div class="desc">Cauliflower, potato and broccoli, golden fried with Gram flour batter</div></div>
  </div>

  <!-- Starters cont. & chef's specials -->
  <div class="panel">
    <div class="item"><div class="row"><span>Keema Singhara</span><span class="code">2</span><span class="price">€5.00</span></div><div class="desc">Spicy seasoned mince lamb in light pastry</div></div>
    <div class="item"><div class="row"><span>Chicken Tikka</span><span class="code">3</span><span class="price">€5.00</span></div><div class="desc">Tender chicken marinated overnight with yoghurt, spices charred in tandoor</div></div>
    <div class="item"><div class="row"><span>Seekh Kebab</span><span class="code"></span><span class="price">€5.50</span></div><div class="desc">Skewered hand pounded lamb glazed in tandoor with green chilli &amp; black cardamom</div></div>
    <div class="item"><div class="row"><span>Chicken Pakora</span><span class="code">3</span><span class="price">€5.00</span></div><div class="desc">Boneless pieces of chicken coated in gram flour batter, with spices</div></div>
    <div class="item"><div class="row"><span>Chicken Wings</span><span class="code">2,1</span><span class="price">€5.00</span></div><div class="desc">Our special marinated wings cooked in the tandoor</div></div>
    <div class="item"><div class="row"><span>Tandoori Mix Meat Platter</span><span class="code">3</span><span class="price">€8.50</span></div><div class="desc">Assortment of tandoori chicken on bone, seekh kebab and chicken tikka</div></div>
    <div class="item"><div class="row"><span>Mix Veg platter</span><span class="code">2</span><span class="price">€6.50</span></div><div class="desc">Veg Samosa, Onion Bhaji, Veg Pakora</div></div>
    <div class="item"><div class="row"><span>Doner Kebab</span><span class="code">2,3,6</span><span class="price">€6.00</span></div><div class="desc">Stripes of minced chicken &amp; beef served with garlic mayo, chilli sauce &amp; mixed salad</div></div>
    <div class="item"><div class="row"><span>Chicken Tikka Kebab</span><span class="code">2,3,6</span><span class="price">€6.50</span></div><div class="desc">Chicken breast marinated in spices, barbecued served with garlic mayo in naan bread</div></div>
    <div class="item"><div class="row"><span>Garlic Chips</span><span class="code"></span><span class="price">€4.00</span></div></div>
    <div class="item"><div class="row"><span>Mix Kebab</span><span class="code">2,3,6</span><span class="price">€6.50</span></div><div class="desc">Pieces of chicken tikka &amp; doner meat with garlic mayo, chilli sauce in naan bread</div></div>
    <div class="section-tag">Chef Arjun's Special Curries</div>
    <div class="item"><div class="row"><span>Butter Murgh</span><span class="code">3,5</span><span class="price">€10.50</span></div><div class="desc">Chicken cooked in tandoor, tossed with rich tomato, cashew sauce, splash of cream with hint of honey &amp; dry fenugreek</div></div>
    <div class="item"><div class="row"><span>Laal Maas</span><span class="code">3</span><span class="price">€11.50</span></div><div class="desc">Traditional rajasthani lamb cooked with garlic and ginger, degi chilli powder, tomatoes finished with star aniseed and cumin powder</div></div>
  </div>

  <!-- Chicken dishes -->
  <div class="panel">
    <div class="item"><div class="row"><span>Shahi Veg Kofta</span><span class="code">3,5</span><span class="price">€10.00</span></div><div class="desc">Handmade veg and paneer dumplings simmered in tomato sauce, lovely fenugreek sauce finished with touch of honey and cream</div></div>
    <div class="item"><div class="row"><span>Kerala Prawn</span><span class="code">14</span><span class="price">€12.00</span></div><div class="desc">Delicacy of kerala spices, tomato and red onion curry finished with touch of fresh coconut</div></div>
    <div class="section-tag">Chicken Dishes</div>
    <div class="item"><div class="row"><span>Punjabi Saag</span><span class="code">3,y</span><span class="price">€8.95</span></div><div class="desc">Chicken cooked with spinach, ginger, garlic, fresh cream &amp; tempered with Punjabi tarka</div></div>
    <div class="item"><div class="row"><span>Royale Korma</span><span class="code">3,5</span><span class="price">€8.95</span></div><div class="desc">Breast of chicken cooked in a rich creamy sauce with saffron &amp; coconut, probably most popular among Irish</div></div>
    <div class="item"><div class="row"><span>Saffron Hearth Chicken Curry</span><span class="code">3,4,5</span><span class="price">€8.95</span></div><div class="desc">Traditional curry cooked with coconut, mustard seed, cashews and curry leaves</div></div>
    <div class="item"><div class="row"><span>Chicken Karahi</span><span class="code"></span><span class="price">€8.95</span></div><div class="desc">Boneless chicken. Prepared in Deg with peppers, onions, tomatoes and Indian whole spices</div></div>
    <div class="item"><div class="row"><span>Chicken Tikka Masala</span><span class="code">3</span><span class="price">€8.95</span></div><div class="desc">Chicken roasted in charcoal and simmered in smooth creamy tomato sauce with pulled fenugreek leaves and jaggery</div></div>
    <div class="item"><div class="row"><span>South Indian Garlic Chilli</span><span class="code"></span><span class="price">€8.95</span></div><div class="desc">Chicken cooked in south Indian style and loaded with garlic, ground spices, fresh herbs</div></div>
    <div class="item"><div class="row"><span>Chicken Dahiwala</span><span class="code">3</span><span class="price">€8.95</span></div><div class="desc">Amazingly spicy chicken curry cooked with yogurt, green chillies, ginger and herbs</div></div>
    <div class="item"><div class="row"><span>Murgh Biryani</span><span class="code">3,5,y</span><span class="price">€9.95</span></div><div class="desc">Perfumed basmati rice with chicken cubes, nuts, golden onions and biryani spices, served with sauce</div></div>
    <div class="photo spread" role="img" aria-label="Photo of samosas and curries laid out on a table"></div>
  </div>
</section>

</body>
</html>
```